Lumen Path - Fiber Internet to the home postcard

Design a postcard for my company, Lumen Path, using the logo below. On the front of the card:
- No Buffering • No BS
- Second line should be the logo
- $60 / month • 10-Gigs
- lumenpath.net

Color palate should follow the colors in the logo.

Address should say
- Special pricing during construction
- Our best price
- Our fastest speed
- $60 / month • 10-Gigs
- lumenpath.net

Target Market(s)

25 - 55 year olds. Middle income/class. People with kids and pick up trucks

Industry/Entity Type

Fiber Internet Service Provider

Font styles to use
Sans Serif

Colors

Designer to choose colors to be used in the design.

Requirements
Nice to have
• I am open to more creative changes

```html
<!DOCTYPE html>
<html lang="en">
<head>
<meta charset="utf-8">
<title>Lumen Path – Fiber Postcard</title>
<link href="https://fonts.googleapis.com/css2?family=Jost:wght@500;600;700;800&display=swap" rel="stylesheet">
<style>
  :root {
    --navy: #1c2d5e;
    --navy-deep: #0b1233;
    --ink: #05081a;
    --green: #8dc63f;
    --green-bright: #7ac143;
    --paper: #e3e7ee;
    --page: #e6e7e9;
    --white: #ffffff;
  }
  * { box-sizing: border-box; margin: 0; padding: 0; }
  html, body { width: 1200px; height: 532px; overflow: hidden; }
  body {
    background: var(--page);
    font-family: "Jost", "Century Gothic", sans-serif;
    position: relative;
  }
  .card {
    position: absolute;
    top: 84px;
    width: 510px;
    height: 364px;
    overflow: hidden;
  }

  /* Front */
  .card--front {
    left: 70px;
    background: linear-gradient(120deg, #f1f3f7 0%, #dde2ea 55%, #c7cdd8 100%);
  }
  .tagline-band {
    position: absolute; left: 0; top: 0; width: 100%; height: 56px;
    background: var(--navy);
    color: var(--green);
    font-weight: 600; font-size: 26px; letter-spacing: 0.5px;
    display: flex; align-items: center; justify-content: center;
  }
  .brand-mark {
    position: absolute; left: 30px; top: 78px; width: 465px; height: 130px;
    display: flex; align-items: center; gap: 12px;
  }
  .brand-mark__name {
    color: var(--navy); font-weight: 800; font-size: 62px; line-height: 1; letter-spacing: -1px;
    white-space: nowrap;
  }
  .brand-mark__dot {
    width: 128px; height: 128px; border-radius: 50%;
    background: var(--green-bright); flex: none;
  }
  .family-photo {
    position: absolute; left: 24px; top: 180px; width: 250px; height: 182px;
    background: linear-gradient(170deg, #d6dbe3 0%, #b9c7a8 55%, #9fd13a 100%);
    border-radius: 4px;
  }
  .offer-tile {
    position: absolute; top: 228px; width: 76px; height: 72px;
    background: var(--navy); color: var(--green);
    border-radius: 0 18px 0 0;
    display: flex; flex-direction: column; align-items: center; justify-content: center;
    line-height: 1;
  }
  .offer-tile--price { left: 304px; }
  .offer-tile--speed { left: 388px; }
  .offer-tile__value { font-weight: 600; font-size: 33px; }
  .offer-tile__unit { font-weight: 600; font-size: 15px; margin-top: 4px; }
  .url-bar {
    position: absolute; left: 274px; top: 300px; width: 236px; height: 33px;
    background: var(--green);
    color: var(--navy); font-weight: 600; font-size: 21px;
    display: flex; align-items: center; justify-content: center;
  }

  /* Back */
  .card--back {
    left: 620px;
    background: radial-gradient(ellipse at 50% 95%, #23357a 0%, #121c4d 40%, var(--ink) 85%);
  }
  .network-backdrop {
    position: absolute; left: 0; top: 150px; width: 100%; height: 214px;
    background: radial-gradient(ellipse at 50% 100%, rgba(60,90,170,0.55) 0%, rgba(20,30,80,0.2) 60%, transparent 100%);
  }
  .back-brand {
    position: absolute; left: 0; top: 52px; width: 100%;
    display: flex; align-items: center; justify-content: center; gap: 8px;
  }
  .back-brand__dot { width: 30px; height: 30px; border-radius: 50%; background: var(--green-bright); }
  .back-brand__name { color: var(--green-bright); font-weight: 800; font-size: 38px; line-height: 1; letter-spacing: -0.5px; }
  .promo-heading {
    position: absolute; left: 0; top: 118px; width: 100%;
    color: var(--white); text-align: center; font-weight: 600; font-size: 20px; line-height: 28px;
  }
  .promo-label {
    position: absolute; top: 196px; width: 90px;
    color: var(--white); font-weight: 600; font-size: 23px; line-height: 24px; text-align: right;
  }
  .promo-label--price { left: 40px; }
  .promo-label--speed { left: 238px; }
  .promo-tile {
    position: absolute; top: 190px; width: 97px; height: 92px;
    background: var(--green); color: var(--navy);
    border-radius: 0 22px 0 0;
    display: flex; flex-direction: column; align-items: center; justify-content: center; line-height: 1;
  }
  .promo-tile--price { left: 144px; }
  .promo-tile--speed { left: 342px; }
  .promo-tile__value { font-weight: 600; font-size: 42px; }
  .promo-tile__unit { font-weight: 600; font-size: 18px; margin-top: 5px; }
  .back-url-bar {
    position: absolute; left: 0; top: 298px; width: 100%; height: 35px;
    background: var(--navy);
    color: var(--white); font-weight: 600; font-size: 20px;
    display: flex; align-items: center; justify-content: center;
  }
</style>
</head>
<body>
  <section class="card card--front">
    <div class="tagline-band">•NO BUFFERING • NO BS</div>
    <div class="brand-mark">
      <span class="brand-mark__name">Lumen Path</span>
      <span class="brand-mark__dot"></span>
    </div>
    <div class="family-photo" role="img" aria-label="Family of three relaxing on a lime green sofa, watching a laptop together"></div>
    <div class="offer-tile offer-tile--price">
      <span class="offer-tile__value">$60</span>
      <span class="offer-tile__unit">Month</span>
    </div>
    <div class="offer-tile offer-tile--speed">
      <span class="offer-tile__value">10</span>
      <span class="offer-tile__unit">Gigs</span>
    </div>
    <div class="url-bar">lumenpath.net</div>
  </section>

  <section class="card card--back">
    <div class="network-backdrop" role="img" aria-label="Glowing digital globe with network connection icons"></div>
    <div class="back-brand">
      <span class="back-brand__name">Lumen Path Networks</span>
      <span class="back-brand__dot"></span>
    </div>
    <p class="promo-heading">SPECIAL PRICING<br>DURING CONSTRUCTION</p>
    <p class="promo-label promo-label--price">Our<br>best<br>price</p>
    <div class="promo-tile promo-tile--price">
      <span class="promo-tile__value">$60</span>
      <span class="promo-tile__unit">Month</span>
    </div>
    <p class="promo-label promo-label--speed">Our<br>fastest<br>speed</p>
    <div class="promo-tile promo-tile--speed">
      <span class="promo-tile__value">10</span>
      <span class="promo-tile__unit">Gigs</span>
    </div>
    <div class="back-url-bar">www.lumenpath.net</div>
  </section>
</body>
</html>
```